Lanternfield Systems Bi Fold Brocher

I need a bi fold (front/back page 1 & front/back page 2) color brochure designed to pass out to clients at a convention. My website is lanternfieldsys.com. Please take images and text from the website to create the brochure. Use the products and product descriptions to display what we offer. Use the text and quotes to describe what we do. Make it professional, descriptive, and full of useful information.

Industry/Entity Type

Business Software

Font styles to use
Serif

Colors
00a990
33b8a4
86cfc6
fbf289
0255a3
3377b5
85acd3

Requirements
Must have
• Contact Info:
• Address:
• 287 Willowbend Avenue
• Building 700, Suite 3182
• Cumming, GA 30987
• Telephone: 1 (555) 482.7106
• Toll Free: 1 (800) 555.0147
• Email: contact@lanternfieldsys.com
Nice to have
• Good backrounds

```html
<!DOCTYPE html>
<html lang="en">
<head>
<meta charset="utf-8">
<title>Lanternfield Systems Brochure</title>
<link rel="stylesheet" href="https://fonts.googleapis.com/css2?family=Merriweather:wght@300;900&family=Source+Serif+4:wght@400;600;700&display=swap">
<style>
:root{
  --navy:#0f2d4f;
  --ink:#1b1b1b;
  --blue-text:#17386a;
  --teal-light:#86cfc6;
  --teal:#33b8a4;
  --band:#163556;
  --rule:#c9c9c9;
  --sky-top:#cfe0ef;
  --sky-bottom:#f4f8fb;
}
*{margin:0;padding:0;box-sizing:border-box}
html,body{width:1200px;height:848px;overflow:hidden;background:#fff}
body{font-family:"Source Serif 4",Georgia,serif;color:var(--ink);position:relative}
.page{position:absolute;top:0;height:848px;width:600px;background:#fff;overflow:hidden}
.page-left{left:0}
.page-right{left:600px;border-left:1px solid #9a9a9a}
.title{position:absolute;font-family:"Merriweather",Georgia,serif;font-weight:900;color:var(--navy);font-size:39px;letter-spacing:-1px;line-height:1;white-space:nowrap}
.title .light{font-weight:300;color:var(--teal-light);letter-spacing:-.5px}
.corp-title{left:46px;top:70px}
.product-title{left:52px;top:446px}
.features-title{right:26px;top:74px}
.bullets{position:absolute;left:72px;top:128px;width:470px;list-style:none;font-size:11.8px;line-height:17.4px}
.bullets li{position:relative;padding-left:13px;margin-bottom:3.6px}
.bullets li svg{position:absolute;left:0;top:5px;width:8px;height:8px}
.clients{position:absolute;left:88px;top:368px;display:flex;align-items:center;gap:15px;font-size:9.5px;font-weight:700;color:var(--ink)}
.client{display:flex;align-items:center;gap:4px;white-space:nowrap}
.client i{width:14px;height:14px;border-radius:50%;background:#5a6a7c;display:inline-block}
.sky{position:absolute;left:300px;top:480px;width:300px;height:368px;background:linear-gradient(180deg,var(--sky-top),var(--sky-bottom) 70%)}
.computer{position:absolute;left:84px;top:516px;width:156px;height:154px;background:linear-gradient(160deg,#e8ecef,#b9c3cb);border-radius:6px}
.band{position:absolute;left:0;top:672px;width:288px;height:42px;background:var(--band);color:#fff;font-weight:600;font-size:16px;padding:11px 0 0 50px}
.product-box{position:absolute;left:330px;top:500px;width:241px;border:1px solid #222;background:#fff;font-size:10.4px;line-height:15.6px;color:#333}
.product-box p{padding:5px 8px 8px;border-bottom:1px solid #222}
.product-box p:last-child{border-bottom:none;padding-bottom:14px}
.tech-label{position:absolute;left:79px;top:752px;font-size:13.5px;font-weight:600;color:#222}
.tech{position:absolute;left:82px;top:788px;display:flex;gap:20px;font-size:11px;font-weight:700;color:#3a3a3a}
.tech span{white-space:nowrap}
.device{position:absolute;left:62px;top:134px;width:256px;height:202px;background:linear-gradient(180deg,#1d2328,#3b4650);border-radius:6px}
.intro{position:absolute;left:338px;top:132px;width:232px;font-size:13px;line-height:15.8px;color:var(--blue-text)}
.photo{position:absolute;top:404px;width:139px;height:104px}
.photo-1{left:64px;background:linear-gradient(160deg,#c9c7bd,#3c3f3e)}
.photo-2{left:229px;background:linear-gradient(160deg,#9b9788,#c7b244)}
.photo-3{left:393px;background:linear-gradient(160deg,#d8dadb,#2b2e31)}
.caption{position:absolute;top:524px;width:132px;font-size:9.8px;line-height:12px;color:var(--blue-text)}
.caption-1{left:64px}
.caption-2{left:231px}
.caption-3{left:393px}
.divider{position:absolute;top:520px;width:1px;height:136px;background:var(--rule)}
.divider-1{left:218px}
.divider-2{left:381px}
.edi{position:absolute;left:64px;top:696px;width:306px;font-size:13.6px;line-height:16.4px;color:var(--blue-text)}
.edi-art{position:absolute;left:375px;top:690px;width:166px;height:86px;border-radius:8px;background:linear-gradient(135deg,#5fa8e0,#f4a259)}
.contact{position:absolute;left:64px;top:790px;width:480px;display:flex;gap:28px;font-size:9.8px;line-height:12.6px;color:var(--blue-text);border-top:1px solid var(--rule);padding-top:6px}
.contact strong{font-weight:700;color:var(--navy)}
</style>
</head>
<body>
<section class="page page-left">
  <h1 class="title corp-title">Corporate <span class="light">Overview</span></h1>
  <ul class="bullets">
    <li><svg viewBox="0 0 8 8"><path d="M1 4l2 2 4-5" fill="none" stroke="#222" stroke-width="1.4"/></svg>Founded as a result of direct experience owning and managing a rail yard.</li>
    <li><svg viewBox="0 0 8 8"><path d="M1 4l2 2 4-5" fill="none" stroke="#222" stroke-width="1.4"/></svg>Software cost must be scalable to the terminal that is using it.</li>
    <li><svg viewBox="0 0 8 8"><path d="M1 4l2 2 4-5" fill="none" stroke="#222" stroke-width="1.4"/></svg>Open the lower end market and provide competitive pricing for the higher end market.</li>
    <li><svg viewBox="0 0 8 8"><path d="M1 4l2 2 4-5" fill="none" stroke="#222" stroke-width="1.4"/></svg>Prepare our client to use the software and understand its functionality. The transition to our software must be easy and seamless. The client needs to understand completely and confidently how to use the software before purchasing it.</li>
    <li><svg viewBox="0 0 8 8"><path d="M1 4l2 2 4-5" fill="none" stroke="#222" stroke-width="1.4"/></svg>Confirm and determine that the client understands the cost of the software upfront.</li>
    <li>Continue to grow our client base while never loosing the commitment to providing quick, honest answers, and cost effective solutions.</li>
    <li><svg viewBox="0 0 8 8"><path d="M1 4l2 2 4-5" fill="none" stroke="#222" stroke-width="1.4"/></svg>Our current clients will attest to and our future clients will unquestionably receive the most user-friendly and robust software solutions available to manage their rail terminals.</li>
  </ul>
  <div class="clients">
    <span class="client"><i></i>Veltmark Motors</span>
    <span class="client">Korrin Auto</span>
    <span class="client">Trackside Loading</span>
    <span class="client">Harlow Grain</span>
    <span class="client">Crossline Transfer</span>
    <span class="client">Northway Paper</span>
  </div>

  <h2 class="title product-title">Product <span class="light">Overview</span></h2>
  <div class="sky" role="img" aria-label="Soft sky and sea backdrop"></div>
  <div class="computer" role="img" aria-label="Illustration of a desktop computer running Lanternfield Systems with a wireless signal"></div>
  <div class="band">Web-Based Application</div>
  <div class="product-box">
    <p>Easily operated and strait forward dashboard with drop down menus for uncomplicated management of your rail terminal.</p>
    <p>Detailed inspection component with current and state of the art easy to use technology.</p>
    <p>Compelling transloading software. Mobile Data Collection, ERP Integration, Custom Ad-Hoc Reporting, Transload Customer Portal, and Scale House Integration.</p>
    <p>Comprehensive and accurate corporate reporting</p>
  </div>
  <div class="tech-label">Technology</div>
  <div class="tech">
    <span>Scriptor</span><span>TableBase</span><span>Orbix</span><span>Nimbus Cloud</span><span>Brewcode</span><span>Quillserve</span><span>Stratos OS</span>
  </div>
</section>

<section class="page page-right">
  <h2 class="title features-title">Software <span class="light">Features</span></h2>
  <div class="device" role="img" aria-label="Desktop monitor and tablet showing the rail car inventory dashboard"></div>
  <p class="intro">Know where every rail car is all the time. Managing rail car locations within your terminal becomes simple and fast using our web-based or tablet application.</p>

  <div class="photo photo-1" role="img" aria-label="Photo of a locomotive on snowy tracks"></div>
  <div class="photo photo-2" role="img" aria-label="Photo of a worker inspecting a railcar"></div>
  <div class="photo photo-3" role="img" aria-label="Photo of tank cars lined up in a rail yard"></div>
  <div class="divider divider-1"></div>
  <div class="divider divider-2"></div>
  <p class="caption caption-1">Manage rail transloading activities to and from a truck or vessel. The software allows the transload terminal operation to effectively and efficiently manage each transaction, decrease paper processing, and provide customers with live inventory and access to transactions.</p>
  <p class="caption caption-2">Automated railcar inspections are now affordable and reliable. You can create unlimited inspection forms and assign specific inspections to individual users. No more paper, no more going back for photos, and no more sorting through the daily inspection sheets.</p>
  <p class="caption caption-3">Built-in demurrage management functionality that maintains key data to track and respond to demurrage challenges.</p>

  <p class="edi">Lanternfield Systems has built a robust system for handling and generating EDI messages in order to automate data entry and communicate key pieces of data with the carrier.</p>
  <div class="edi-art" role="img" aria-label="Illustration of freight transport around a map with route markers"></div>

  <address class="contact" style="font-style:normal">
    <div><strong>Lanternfield Systems</strong><br>287 Willowbend Avenue<br>Building 700, Suite 3182<br>Cumming, GA 30987</div>
    <div>Telephone: 1 (555) 482.7106<br>Toll Free: 1 (800) 555.0147<br>contact@lanternfieldsys.com<br>lanternfieldsys.com</div>
  </address>
</section>
</body>
</html>
```